Spectacular Business Card Design for AI SAAS Plattform called Pathleap.ai

Hi Creators
I need an outstanding new Design for my business card.
I run an AI automated Saas Plattform Called Pathleap.ai

Front side:
Logo
Slogan: DIY Business Development & Social Media Management
Data:
Name: Markus Velbringer - CEO / Founder
email: m.velbringer@pathleap-example.ai
mobile: +43 699 82 37 915

Company name:
Pathleap FlexCo

Backside:

What we stand for Slogan:
Vertrauen in KI-Technologie, getragen von menschlicher Vision: Dein Sprung nach vorn!
+ a fancy design what captures our core competencies - AI automisations, Social Media Management, Business development
(dont know if its too much, but AI and social media should be )

pls find attached the logo and the old design

Industry/Entity Type

AI automations for marketing and business development

Contact Information for Business Card

Front side: Logo Slogan: DIY Business Development & Social Media Management Data: Name: Markus Velbringer - CEO / Founder email: m.velbringer@pathleap-example.ai mobile: +43 699 82 37 915 Company name: Pathleap FlexCo Backside: What we stand for Slogan: Vertrauen in KI-Technologie, getragen von menschlicher Vision: Dein Sprung nach vorn!

Font styles to use
Serif
Sans Serif

Requirements
Nice to have
• a fancy design on the backside, a fancy design what captures our core competencies - AI automisations, Social Media Management, Business development

```html
<!DOCTYPE html>
<html lang="en">
<head>
<meta charset="utf-8">
<title>Pathleap.ai – Business Card</title>
<link href="https://fonts.googleapis.com/css2?family=Montserrat:wght@400;500;600;700&display=swap" rel="stylesheet">
<style>
  :root {
    --page-bg: #3a3a3c;
    --teal: #0a89a2;
    --teal-deep: #0c4e62;
    --orange: #f28b25;
    --white: #ffffff;
    --ink-grey: #5a5f63;
    --rule: #0a89a2;
  }
  * { box-sizing: border-box; margin: 0; padding: 0; }
  html, body { width: 1200px; height: 689px; overflow: hidden; }
  body {
    background: var(--page-bg);
    font-family: "Montserrat", sans-serif;
    display: flex;
    align-items: center;
    justify-content: center;
    gap: 40px;
  }
  .card {
    width: 540px;
    height: 310px;
    position: relative;
    box-shadow: 0 10px 30px rgba(0,0,0,.45);
  }

  /* Back side */
  .card--back {
    background: var(--teal);
    color: var(--white);
    display: flex;
    flex-direction: column;
    align-items: center;
    justify-content: center;
    text-align: center;
    padding: 0 40px;
  }
  .brand {
    display: flex;
    align-items: center;
    gap: 12px;
    font-weight: 600;
    letter-spacing: .5px;
  }
  .brand__mark { width: 18px; height: 18px; }
  .card--back .brand { font-size: 40px; color: var(--teal-deep); margin-bottom: 26px; }
  .card--back .brand__mark { background: var(--teal-deep); }
  .slogan-label { color: var(--orange); font-weight: 600; font-size: 14px; margin-bottom: 6px; }
  .slogan-text { font-size: 13.5px; line-height: 1.55; }
  .slogan-text .accent { color: var(--orange); }
  .competencies { font-size: 13px; line-height: 1.55; margin-top: 6px; }

  /* Front side */
  .card--front {
    background: var(--white);
    display: grid;
    grid-template-columns: 230px 1px 1fr;
    grid-template-rows: 1fr auto;
    column-gap: 28px;
    padding: 36px 32px 26px;
  }
  .card--front .brand {
    font-size: 38px;
    color: var(--teal);
    align-self: center;
    justify-self: center;
  }
  .card--front .brand__mark { background: var(--orange); }
  .divider { background: var(--rule); height: 150px; align-self: center; }
  .contact { align-self: center; }
  .contact__name { color: var(--teal); font-weight: 700; font-size: 19px; }
  .contact__role { color: var(--ink-grey); font-size: 13px; margin-top: 2px; }
  .contact__company { color: var(--teal); font-weight: 600; font-size: 13px; margin: 14px 0 12px; }
  .contact__list { list-style: none; }
  .contact__item {
    display: flex; align-items: center; gap: 9px;
    color: var(--ink-grey); font-size: 12.5px; line-height: 1.75;
  }
  .contact__icon { width: 12px; height: 12px; fill: var(--orange); flex: none; }
  .tagline {
    grid-column: 1 / -1;
    text-align: center;
    color: var(--ink-grey);
    font-size: 13.5px;
    letter-spacing: .3px;
  }
</style>
</head>
<body>

  <section class="card card--back" aria-label="Card back side">
    <div class="brand"><span class="brand__mark"></span>Pathleap</div>
    <p class="slogan-label">What we stand for Slogan:</p>
    <p class="slogan-text">Vertrauen in KI-Technologie, getragen von menschlicher<br>
      <span class="accent">Vision:</span> Dein Sprung nach vorn!</p>
    <p class="competencies">+ a fancy design what captures our core competencies -<br>
      AI automisations, Social Media Management, Business development</p>
  </section>

  <section class="card card--front" aria-label="Card front side">
    <div class="brand"><span class="brand__mark"></span>Pathleap</div>
    <div class="divider"></div>
    <div class="contact">
      <p class="contact__name">Markus Velbringer</p>
      <p class="contact__role">CEO / Founder</p>
      <p class="contact__company">Pathleap FlexCo</p>
      <ul class="contact__list">
        <li class="contact__item">
          <svg class="contact__icon" viewBox="0 0 24 24" aria-hidden="true"><path d="M6.6 10.8a15 15 0 0 0 6.6 6.6l2.2-2.2a1 1 0 0 1 1-.25 11.4 11.4 0 0 0 3.6.57 1 1 0 0 1 1 1V20a1 1 0 0 1-1 1A17 17 0 0 1 3 4a1 1 0 0 1 1-1h3.5a1 1 0 0 1 1 1c0 1.25.2 2.45.57 3.57a1 1 0 0 1-.25 1z"/></svg>
          +43 699 82 37 915
        </li>
        <li class="contact__item">
          <svg class="contact__icon" viewBox="0 0 24 24" aria-hidden="true"><path d="M2 5h20v14H2z M2 5l10 8 10-8" fill="var(--orange)"/><path d="M3 6l9 7 9-7" fill="none" stroke="#fff" stroke-width="1.6"/></svg>
          m.velbringer@pathleap-example.ai
        </li>
        <li class="contact__item">
          <svg class="contact__icon" viewBox="0 0 24 24" aria-hidden="true"><circle cx="12" cy="12" r="10"/><path d="M2 12h20M12 2c3 3 3 17 0 20M12 2c-3 3-3 17 0 20" fill="none" stroke="#fff" stroke-width="1.4"/></svg>
          www.pathleap-example.ai
        </li>
      </ul>
    </div>
    <p class="tagline">DIY Business Development &amp; Social Media Management</p>
  </section>

</body>
</html>
```